Phuket Thailand - Rental Villa Website

I have a villa for rent in Thailand and require a website - i need to demo pictures/walk through video, local attractions, villa facilities description plus seaonal rates and online booking.

Industry/Entity Type

Rental

Coding

Coded - Design and coding required

```html
<!DOCTYPE html>
<html lang="en">
<head>
<meta charset="utf-8">
<title>Andaman Villas – Accommodation for Rent</title>
<link rel="stylesheet" href="https://fonts.googleapis.com/css2?family=Montserrat:wght@400;600;700;800&family=Noto+Serif:ital,wght@0,400;0,700;1,400&display=swap">
<style>
:root{
  --orange:#e8580c;
  --orange-light:#f27b2c;
  --ink:#222;
  --muted:#666;
  --line:#dcdcdc;
  --tick:#4cb96a;
  --footer:#1d1d1d;
  --footer-text:#d4d4d4;
  --white:#fff;
}
*{box-sizing:border-box;margin:0;padding:0}
html,body{width:1200px;height:3082px;overflow:hidden}
body{font-family:"Noto Serif",serif;color:var(--ink);background:var(--white);position:relative}
.sans{font-family:"Montserrat",sans-serif}
.btn{display:inline-block;background:var(--orange);color:var(--white);font-family:"Montserrat",sans-serif;font-weight:700;font-size:11px;letter-spacing:.5px;text-transform:uppercase;border-radius:16px;text-align:center;box-shadow:0 3px 5px rgba(0,0,0,.25)}

/* hero */
.hero{position:absolute;left:0;top:0;width:1200px;height:561px;background:linear-gradient(180deg,#2b3744 0%,#3d5160 35%,#32534f 60%,#2c4a3c 100%)}
.hero-photo{position:absolute;inset:0;background:radial-gradient(ellipse at 75% 45%,rgba(190,160,100,.35),transparent 45%),radial-gradient(ellipse at 20% 75%,rgba(80,140,120,.4),transparent 55%)}
.nav{position:absolute;top:32px;left:164px;right:164px;display:flex;justify-content:space-between;align-items:center}
.brand{font-family:"Montserrat",sans-serif;font-weight:700;font-size:17px;color:var(--white);letter-spacing:.3px}
.menu{display:flex;gap:26px;list-style:none}
.menu li{font-family:"Montserrat",sans-serif;font-weight:600;font-size:11.5px;color:var(--white);text-transform:uppercase}
.hero-title{position:absolute;top:238px;left:390px;width:660px;text-align:center;font-family:"Montserrat",sans-serif;font-weight:700;font-size:41px;color:var(--white);letter-spacing:.5px}
.hero-sub{position:absolute;top:290px;left:500px;width:540px;text-align:right;font-style:italic;font-size:15px;color:var(--white)}
.hero-rule{position:absolute;top:328px;left:339px;width:699px;height:1px;background:rgba(255,255,255,.7)}
.hero-price{position:absolute;top:339px;left:845px;width:190px;height:44px;line-height:44px;border-radius:22px;font-size:12px}
.hero-price b{font-size:25px;margin-left:10px;vertical-align:-3px}
.arrow{position:absolute;top:263px;width:37px;height:37px;border:2px solid var(--white)}
.arrow svg{display:block;margin:10px auto}

/* destinations */
.destinations{position:absolute;top:647px;left:166px;display:flex;gap:24px}
.dest{position:relative;width:274px;height:270px;box-shadow:0 3px 8px rgba(0,0,0,.35);border:4px solid var(--white);text-align:center;color:var(--white)}
.dest-photo{position:absolute;inset:0}
.dest-body{position:relative;padding-top:100px}
.dest-name{font-weight:700;font-size:22px;text-transform:uppercase;text-shadow:0 2px 4px rgba(0,0,0,.5)}
.dest-from{font-family:"Montserrat",sans-serif;font-size:9px;font-weight:700;margin-top:2px}
.dest-price{font-weight:700;font-size:18px;text-shadow:0 2px 4px rgba(0,0,0,.5)}
.dest .btn{margin-top:22px;width:124px;height:28px;line-height:28px;font-size:10px}

/* about band */
.about{position:absolute;top:1015px;left:0;width:1200px;height:366px;background:linear-gradient(90deg,#2c3128,#4a4c44 40%,#57503f 70%,#2e2f2a)}
.about-overlay{position:absolute;inset:0;background:rgba(0,0,0,.35)}
.video{position:absolute;top:80px;left:166px;width:389px;height:206px;background:linear-gradient(180deg,#dfe9f2 0%,#f3f3f0 45%,#c47a3d 60%,#5f8a4a 85%)}
.play{position:absolute;left:160px;top:68px}
.perks{position:absolute;top:100px;left:620px;list-style:none}
.perks li{display:flex;align-items:center;gap:14px;font-size:13px;color:var(--white);height:27.5px}
.about .btn{position:absolute;top:249px;left:620px;width:124px;height:28px;line-height:28px}

/* listings */
.listings{position:absolute;top:1467px;left:166px;width:868px}
.listing{display:flex;height:272px;border:1px solid var(--line);margin-bottom:21px;background:var(--white);box-shadow:0 1px 3px rgba(0,0,0,.08)}
.listing.reverse{flex-direction:row-reverse}
.listing-photo{width:417px;height:100%;flex:none}
.listing-body{flex:1;padding:24px 30px}
.listing-title{font-family:"Montserrat",sans-serif;font-weight:700;font-size:17px}
.listing-text{font-size:11px;line-height:18px;color:var(--muted);margin-top:8px;width:390px}
.listing-meta{display:flex;align-items:center;gap:8px;margin-top:12px}
.tag{border:1px solid var(--line);box-shadow:0 1px 2px rgba(0,0,0,.15);font-size:10px;padding:5px 12px}
.price{margin-left:12px;color:var(--orange);font-weight:700;font-size:19px}
.price small{font-family:"Montserrat",sans-serif;font-size:9px;margin-right:10px}
.features{display:grid;grid-template-columns:170px 170px;margin-top:12px;list-style:none}
.features li{font-size:11px;line-height:15px;display:flex;gap:8px;align-items:center;color:#333}
.listing .btn{margin-top:18px;width:126px;height:28px;line-height:28px}

/* newsletter */
.newsletter{position:absolute;top:2690px;left:0;width:1200px;height:76px;background:linear-gradient(90deg,#e34d0d,#f0742a)}
.newsletter h3{position:absolute;left:164px;top:30px;font-family:"Montserrat",sans-serif;font-weight:700;font-size:14px;color:var(--white);letter-spacing:.3px}
.signup{position:absolute;left:612px;top:16px;width:420px;height:44px;border-radius:22px;background:rgba(255,255,255,.18);border:1px solid rgba(255,255,255,.35);display:flex;align-items:center;padding-left:22px;gap:12px;color:rgba(255,255,255,.9);font-family:"Montserrat",sans-serif;font-size:13px}
.signup .btn{position:absolute;right:6px;top:6px;width:86px;height:30px;line-height:30px;font-size:9.5px;background:rgba(255,255,255,.18);box-shadow:none;border:1px solid rgba(255,255,255,.35)}

/* footer */
.footer{position:absolute;top:2766px;left:0;width:1200px;height:316px;background:var(--footer);color:var(--footer-text);font-family:"Montserrat",sans-serif}
.footer-top-rule{position:absolute;top:104px;left:166px;width:868px;height:1px;background:#2c2c2c}
.col{position:absolute;top:90px}
.col h4{font-size:11.5px;font-weight:700;color:var(--white);text-transform:uppercase;text-decoration:underline;text-underline-offset:3px;margin-bottom:14px}
.col ul{list-style:none}
.col li{font-size:11px;line-height:18px}
.col p{font-size:11px;line-height:18px;width:220px}
.socials{display:flex;gap:14px;margin-top:16px}
.socials span{width:16px;height:16px;border-radius:50%;background:var(--white)}
.footer-brand{position:absolute;top:180px;left:862px;font-size:16px;font-weight:700;color:var(--white)}
.footer-rule{position:absolute;top:244px;left:166px;width:868px;height:1px;background:#2e2e2e}
.legal{position:absolute;top:266px;left:0;width:1200px;text-align:center;font-size:10px}
.legal span{margin:0 8px}
</style>
</head>
<body>

<header class="hero">
  <div class="hero-photo" role="img" aria-label="Evening view of a resort swimming pool with palm trees, terrace columns and potted flowers"></div>
  <nav class="nav">
    <div class="brand">ANDAMAN VILLAS</div>
    <ul class="menu">
      <li>Home</li><li>About us</li><li>Find apartments</li><li>Blog</li><li>Our gallery</li><li>Contacts</li>
    </ul>
  </nav>
  <div class="arrow" style="left:51px"><svg width="12" height="14" viewBox="0 0 12 14"><path d="M9 1 3 7l6 6" fill="none" stroke="#fff" stroke-width="2.5"/></svg></div>
  <div class="arrow" style="left:1112px"><svg width="12" height="14" viewBox="0 0 12 14"><path d="M3 1l6 6-6 6" fill="none" stroke="#fff" stroke-width="2.5"/></svg></div>
  <h1 class="hero-title">ACCOMMODATION FOR RENT</h1>
  <p class="hero-sub">Come take a walk with us and expore the city of Stockholm.</p>
  <div class="hero-rule"></div>
  <div class="btn hero-price">FROM <b>$ 1'354</b></div>
</header>

<section class="destinations">
  <article class="dest">
    <div class="dest-photo" role="img" aria-label="Barcelona skyline with a tall tower" style="background:linear-gradient(180deg,#4d7fb3 0%,#8aa4bd 40%,#7a6a5c 70%,#5a4a3e)"></div>
    <div class="dest-body"><div class="dest-name">Barcelona</div><div class="dest-from">FROM</div><div class="dest-price">$ 1000</div><span class="btn">Lear more</span></div>
  </article>
  <article class="dest">
    <div class="dest-photo" role="img" aria-label="Turkish resort pool with palm trees and a water slide" style="background:linear-gradient(180deg,#5a96cf 0%,#9cc0d8 40%,#3fa9b8 70%,#2a8ea6)"></div>
    <div class="dest-body"><div class="dest-name">Turkey</div><div class="dest-from">FROM</div><div class="dest-price">$ 1000</div><span class="btn">Lear more</span></div>
  </article>
  <article class="dest">
    <div class="dest-photo" role="img" aria-label="Egyptian pyramid in the desert under a blue sky" style="background:linear-gradient(180deg,#5a8bc4 0%,#a9bfd6 40%,#b9915f 60%,#c9a472)"></div>
    <div class="dest-body"><div class="dest-name">Egypt</div><div class="dest-from">FROM</div><div class="dest-price">$ 1000</div><span class="btn">Lear more</span></div>
  </article>
</section>

<section class="about">
  <div class="about-overlay" role="img" aria-label="Modern villa with timber cladding and garden at dusk"></div>
  <div class="video" role="img" aria-label="Walk-through video of a modern white villa with pool">
    <svg class="play" width="68" height="68" viewBox="0 0 68 68"><circle cx="34" cy="34" r="33" fill="rgba(30,30,30,.75)"/><path d="M27 22l20 12-20 12z" fill="#fff"/></svg>
  </div>
  <ul class="perks">
    <li><svg width="14" height="14" viewBox="0 0 14 14"><rect x=".5" y=".5" width="13" height="13" fill="none" stroke="#fff"/><path d="M3 7l3 3 5-6" fill="none" stroke="#fff" stroke-width="1.8"/></svg>The market leader in real estate since 2003</li>
    <li><svg width="14" height="14" viewBox="0 0 14 14"><rect x=".5" y=".5" width="13" height="13" fill="none" stroke="#fff"/><path d="M3 7l3 3 5-6" fill="none" stroke="#fff" stroke-width="1.8"/></svg>Awards Real Estate Company, 2010, 2011, 2013</li>
    <li><svg width="14" height="14" viewBox="0 0 14 14"><rect x=".5" y=".5" width="13" height="13" fill="none" stroke="#fff"/><path d="M3 7l3 3 5-6" fill="none" stroke="#fff" stroke-width="1.8"/></svg>More than 200 satisfied customers premium segment</li>
    <li><svg width="14" height="14" viewBox="0 0 14 14"><rect x=".5" y=".5" width="13" height="13" fill="none" stroke="#fff"/><path d="M3 7l3 3 5-6" fill="none" stroke="#fff" stroke-width="1.8"/></svg>We focus only on new buildings and high level</li>
    <li><svg width="14" height="14" viewBox="0 0 14 14"><rect x=".5" y=".5" width="13" height="13" fill="none" stroke="#fff"/><path d="M3 7l3 3 5-6" fill="none" stroke="#fff" stroke-width="1.8"/></svg>Working directly with developers - so have more</li>
  </ul>
  <span class="btn">View all</span>
</section>

<section class="listings">
  <article class="listing">
    <div class="listing-photo" role="img" aria-label="Row of white villas beside a long swimming pool" style="background:linear-gradient(180deg,#5f93c9 0%,#c9d6de 35%,#a59a88 60%,#3e6a74)"></div>
    <div class="listing-body">
      <h2 class="listing-title">RAW10112: Premium 3 Bedroom Villas in Rawai</h2>
      <p class="listing-text">R993 – This modern brand new apartment is located on the 8th floor has a living area of 30sqm, with mountain views. Most would probably agree its the best studio...</p>
      <div class="listing-meta"><span class="tag">Layan Villa</span><span class="tag">Villa/House</span><span class="tag">4 Bedrooms</span><span class="price"><small>FROM</small>$ 1000</span></div>
      <ul class="features"><li><svg width="9" height="8" viewBox="0 0 9 8"><path d="M1 4l2.5 2.5L8 1" fill="none" stroke="#4cb96a" stroke-width="1.8"/></svg>Outdoor swimming pool</li><li><svg width="9" height="8" viewBox="0 0 9 8"><path d="M1 4l2.5 2.5L8 1" fill="none" stroke="#4cb96a" stroke-width="1.8"/></svg>Bar</li><li><svg width="9" height="8" viewBox="0 0 9 8"><path d="M1 4l2.5 2.5L8 1" fill="none" stroke="#4cb96a" stroke-width="1.8"/></svg>Restaurant</li><li><svg width="9" height="8" viewBox="0 0 9 8"><path d="M1 4l2.5 2.5L8 1" fill="none" stroke="#4cb96a" stroke-width="1.8"/></svg>Snack bar</li><li><svg width="9" height="8" viewBox="0 0 9 8"><path d="M1 4l2.5 2.5L8 1" fill="none" stroke="#4cb96a" stroke-width="1.8"/></svg>Sun Terrace</li><li><svg width="9" height="8" viewBox="0 0 9 8"><path d="M1 4l2.5 2.5L8 1" fill="none" stroke="#4cb96a" stroke-width="1.8"/></svg>24 hour Reception</li></ul>
      <span class="btn">More details</span>
    </div>
  </article>
  <article class="listing reverse">
    <div class="listing-photo" role="img" aria-label="Busy Bangkok street with colourful signs and tuk-tuks" style="background:linear-gradient(135deg,#3a4d6e 0%,#b2423c 35%,#3e6b8a 60%,#5a4a3a)"></div>
    <div class="listing-body">
      <h2 class="listing-title">RAW10112: Premium 3 Bedroom Villas in Rawai</h2>
      <p class="listing-text">R993 – This modern brand new apartment is located on the 8th floor has a living area of 30sqm, with mountain views. Most would probably agree its the best studio...</p>
      <div class="listing-meta"><span class="tag">Layan Villa</span><span class="tag">Villa/House</span><span class="tag">4 Bedrooms</span><span class="price"><small>FROM</small>$ 1000</span></div>
      <ul class="features"><li><svg width="9" height="8" viewBox="0 0 9 8"><path d="M1 4l2.5 2.5L8 1" fill="none" stroke="#4cb96a" stroke-width="1.8"/></svg>Outdoor swimming pool</li><li><svg width="9" height="8" viewBox="0 0 9 8"><path d="M1 4l2.5 2.5L8 1" fill="none" stroke="#4cb96a" stroke-width="1.8"/></svg>Bar</li><li><svg width="9" height="8" viewBox="0 0 9 8"><path d="M1 4l2.5 2.5L8 1" fill="none" stroke="#4cb96a" stroke-width="1.8"/></svg>Restaurant</li><li><svg width="9" height="8" viewBox="0 0 9 8"><path d="M1 4l2.5 2.5L8 1" fill="none" stroke="#4cb96a" stroke-width="1.8"/></svg>Snack bar</li><li><svg width="9" height="8" viewBox="0 0 9 8"><path d="M1 4l2.5 2.5L8 1" fill="none" stroke="#4cb96a" stroke-width="1.8"/></svg>Sun Terrace</li><li><svg width="9" height="8" viewBox="0 0 9 8"><path d="M1 4l2.5 2.5L8 1" fill="none" stroke="#4cb96a" stroke-width="1.8"/></svg>24 hour Reception</li></ul>
      <span class="btn">More details</span>
    </div>
  </article>
  <article class="listing">
    <div class="listing-photo" role="img" aria-label="Lit villa at night with a glowing blue pool" style="background:linear-gradient(180deg,#1d3f7a 0%,#5d3a2a 40%,#c06a2e 60%,#1ba6c7 85%)"></div>
    <div class="listing-body">
      <h2 class="listing-title">RAW10112: Premium 3 Bedroom Villas in Rawai</h2>
      <p class="listing-text">R993 – This modern brand new apartment is located on the 8th floor has a living area of 30sqm, with mountain views. Most would probably agree its the best studio...</p>
      <div class="listing-meta"><span class="tag">Layan Villa</span><span class="tag">Villa/House</span><span class="tag">4 Bedrooms</span><span class="price"><small>FROM</small>$ 1000</span></div>
      <ul class="features"><li><svg width="9" height="8" viewBox="0 0 9 8"><path d="M1 4l2.5 2.5L8 1" fill="none" stroke="#4cb96a" stroke-width="1.8"/></svg>Outdoor swimming pool</li><li><svg width="9" height="8" viewBox="0 0 9 8"><path d="M1 4l2.5 2.5L8 1" fill="none" stroke="#4cb96a" stroke-width="1.8"/></svg>Bar</li><li><svg width="9" height="8" viewBox="0 0 9 8"><path d="M1 4l2.5 2.5L8 1" fill="none" stroke="#4cb96a" stroke-width="1.8"/></svg>Restaurant</li><li><svg width="9" height="8" viewBox="0 0 9 8"><path d="M1 4l2.5 2.5L8 1" fill="none" stroke="#4cb96a" stroke-width="1.8"/></svg>Snack bar</li><li><svg width="9" height="8" viewBox="0 0 9 8"><path d="M1 4l2.5 2.5L8 1" fill="none" stroke="#4cb96a" stroke-width="1.8"/></svg>Sun Terrace</li><li><svg width="9" height="8" viewBox="0 0 9 8"><path d="M1 4l2.5 2.5L8 1" fill="none" stroke="#4cb96a" stroke-width="1.8"/></svg>24 hour Reception</li></ul>
      <span class="btn">More details</span>
    </div>
  </article>
  <article class="listing reverse">
    <div class="listing-photo" role="img" aria-label="Warm hotel bedroom with wooden walls and a sea view window" style="background:linear-gradient(135deg,#3b1f16 0%,#8a4a2e 40%,#c9562c 65%,#3d6f8a)"></div>
    <div class="listing-body">
      <h2 class="listing-title">RAW10112: Premium 3 Bedroom Villas in Rawai</h2>
      <p class="listing-text">R993 – This modern brand new apartment is located on the 8th floor has a living area of 30sqm, with mountain views. Most would probably agree its the best studio...</p>
      <div class="listing-meta"><span class="tag">Layan Villa</span><span class="tag">Villa/House</span><span class="tag">4 Bedrooms</span><span class="price"><small>FROM</small>$ 1000</span></div>
      <ul class="features"><li><svg width="9" height="8" viewBox="0 0 9 8"><path d="M1 4l2.5 2.5L8 1" fill="none" stroke="#4cb96a" stroke-width="1.8"/></svg>Outdoor swimming pool</li><li><svg width="9" height="8" viewBox="0 0 9 8"><path d="M1 4l2.5 2.5L8 1" fill="none" stroke="#4cb96a" stroke-width="1.8"/></svg>Bar</li><li><svg width="9" height="8" viewBox="0 0 9 8"><path d="M1 4l2.5 2.5L8 1" fill="none" stroke="#4cb96a" stroke-width="1.8"/></svg>Restaurant</li><li><svg width="9" height="8" viewBox="0 0 9 8"><path d="M1 4l2.5 2.5L8 1" fill="none" stroke="#4cb96a" stroke-width="1.8"/></svg>Snack bar</li><li><svg width="9" height="8" viewBox="0 0 9 8"><path d="M1 4l2.5 2.5L8 1" fill="none" stroke="#4cb96a" stroke-width="1.8"/></svg>Sun Terrace</li><li><svg width="9" height="8" viewBox="0 0 9 8"><path d="M1 4l2.5 2.5L8 1" fill="none" stroke="#4cb96a" stroke-width="1.8"/></svg>24 hour Reception</li></ul>
      <span class="btn">More details</span>
    </div>
  </article>
</section>

<section class="newsletter">
  <h3>SIGN UP FOR EXCLUSIVE SALES AND PRODUCT NEWS</h3>
  <div class="signup">
    <svg width="14" height="11" viewBox="0 0 14 11"><rect x=".5" y=".5" width="13" height="10" fill="none" stroke="#fff"/><path d="M.5 .5 7 6l6.5-5.5" fill="none" stroke="#fff"/></svg>
    your@email.com
    <span class="btn">Subscribe</span>
  </div>
</section>

<footer class="footer">
  <div class="col" style="left:168px">
    <h4>Useful links</h4>
    <ul><li>About Us</li><li>Company Timeline</li><li>History</li><li>Services</li><li>Contact Us</li></ul>
  </div>
  <div class="col" style="left:388px">
    <h4>Useful links</h4>
    <ul><li>Ads &amp; Promos 02</li><li>Warehousing</li><li>Logistics</li><li>Project Transport</li><li>Overland Network</li></ul>
  </div>
  <div class="col" style="left:598px">
    <h4>Contact info</h4>
    <p>Address : Coastline Stays, 12 Harbour Lane, Kata</p>
    <p>Email adress = hello@coastlinestays.com</p>
    <p>Phone Number : +66 76 000 200</p>
  </div>
  <div class="col" style="left:886px">
    <h4 style="text-decoration:none;text-transform:none;font-weight:600">Follow us</h4>
    <div class="socials" aria-label="Social networks"><span></span><span></span><span></span><span></span></div>
  </div>
  <div class="footer-brand">ANDAMAN VILLAS</div>
  <div class="footer-rule"></div>
  <p class="legal"><span>Terms of Service -Privacy Policy</span><span>Copyright © All Rights reserved</span></p>
</footer>

</body>
</html>
```